Präsentationsvorlagen für Start-up im Bereich Unternehmensberatung
Zielgruppe
Start-up im Bereich Unternehmensberatung. Zielgruppen sind CEO und HR Verantwortliche in Großunternehmen. Suchen klares, hochwertiges Design eher an Frauen als an Männer gerichtet. Haben bereits Vorlagen erarbeitet, diese sind aber zu technisch orientiert. Erwartet wird eine neue pptx Präsentation
Aufgabenstellung
Bilder / Texte gemäss Website respektive bestehender PPT.

```html
<!DOCTYPE html>
<html lang="de">
<head>
<meta charset="utf-8">
<title>Schlüsselfaktoren – Der Prozess</title>
<link rel="stylesheet" href="https://fonts.googleapis.com/css2?family=Roboto+Condensed:wght@400;500&family=Roboto:wght@300;400;500&display=swap">
<style>
  :root {
    --brand-red: #c00000;
    --accent-red: #e0141e;
    --text-grey: #6b6b6b;
    --page-bg: #ffffff;
    --rule-red: #c8323a;
  }
  html, body {
    margin: 0;
    padding: 0;
    width: 1200px;
    height: 857px;
    overflow: hidden;
    background: var(--page-bg);
  }
  .slide {
    position: absolute;
    left: 45px;
    top: 124px;
    width: 1110px;
    height: 624px;
    background: var(--page-bg);
    box-shadow: 0 0 12px rgba(0, 0, 0, 0.28);
    font-family: "Roboto", Arial, sans-serif;
  }
  .slide-title {
    position: absolute;
    left: 45px;
    top: 38px;
    margin: 0;
    font-family: "Roboto Condensed", "Arial Narrow", sans-serif;
    font-weight: 400;
    font-size: 45px;
    line-height: 1;
    letter-spacing: 0.2px;
    color: var(--brand-red);
  }
  .key-visual {
    position: absolute;
    left: 385px;
    top: 159px;
    width: 272px;
    height: 272px;
    border-radius: 50%;
    background: var(--brand-red);
  }
  .step {
    position: absolute;
  }
  .step-numeral {
    display: flex;
    gap: 5px;
    height: 29px;
    margin-bottom: 11px;
  }
  .step-numeral span {
    display: block;
    width: 6px;
    height: 100%;
    background: var(--accent-red);
  }
  .step-text {
    margin: 0;
    font-weight: 400;
    font-size: 15.5px;
    line-height: 18.2px;
    color: var(--text-grey);
  }
  .step-one   { left: 153px; top: 266px; width: 220px; }
  .step-two   { left: 716px; top: 177px; width: 300px; }
  .step-three { left: 475px; top: 492px; width: 300px; }
  .step-three .step-numeral { margin-left: 4px; }
  .footer-brand {
    position: absolute;
    left: 15px;
    top: 583px;
    font-family: "Roboto Condensed", "Arial Narrow", sans-serif;
    font-weight: 500;
    font-size: 27px;
    line-height: 1;
    color: var(--brand-red);
  }
  .footer-rule {
    position: absolute;
    left: 91px;
    top: 597px;
    width: 964px;
    height: 1px;
    background: var(--rule-red);
  }
  .page-number {
    position: absolute;
    left: 1070px;
    top: 589px;
    font-family: "Roboto", Arial, sans-serif;
    font-weight: 500;
    font-size: 13px;
    color: var(--accent-red);
  }
</style>
</head>
<body>
  <section class="slide">
    <h1 class="slide-title">SCHLÜSSELFAKTOREN | DER PROZESS</h1>

    <div class="key-visual" role="img" aria-label="Rotes rundes Schlüsselloch-Piktogramm als zentrales Motiv des Prozesses"></div>

    <div class="step step-one">
      <div class="step-numeral" aria-label="I"><span></span></div>
      <p class="step-text">Kick-Off Vortrag u.a.&nbsp; am Beispiel von Arbeitspausen “das habe ich mir jetzt aber verdient“</p>
    </div>

    <div class="step step-two">
      <div class="step-numeral" aria-label="II"><span></span><span></span></div>
      <p class="step-text">Der Unterschied zwischen Willenskraft und Vorstellungs-vermögen, oder die Antworten auf die Frage nach dem Warum?</p>
    </div>

    <div class="step step-three">
      <div class="step-numeral" aria-label="III"><span></span><span></span><span></span></div>
      <p class="step-text">Start des 6-monatigen Prozesses</p>
    </div>

    <div class="footer-brand">WEGWERK</div>
    <div class="footer-rule"></div>
    <div class="page-number">13</div>
  </section>
</body>
</html>
```